Velorix Flyer

PROJECT: Digital Flyer for VeloRix

Format
1920 × 1080 px (landscape, optimized for presentations and email)
Deliverables
• PDF
• PNG

About VeloRix
VeloRix is a Dutch B2B software company providing a unified CRM and customer journey platform. We help businesses manage the entire customer lifecycle — from first contact to loyal customer — by centralizing all touchpoints in one system.
What sets us apart:
Extreme ease of use. The system is self-guiding, shows only what's relevant per employee, and requires virtually no training. All channels (email, phone, chat, in-store) come together in one place with automatic task distribution. Built-in AI functions as a smart digital colleague that continuously learns.
Target audience:
Directors and sales managers at B2B companies with multiple customer contact channels.

Goal:
We want to create a flyer that sets us apart from other CRM platform providers. Our aim is to achieve this through simplicity and a professional appearance. The design should reflect our core value: ease of use. The recipient should feel compelled to engage with us — not overwhelmed by information, but intrigued by clarity. Less is more.

Required Text Elements
Headline:
"CRM that adapts to how you work"
Subline:
"Discover how VeloRix simplifies your sales process"
Call-to-action:
"See it in action — book a call"
Contact details:
• hello@velorix.nl
• 023-5718469
• velorix.com

Required Visual Elements
• VeloRix logo (attached)

Design Style
• Modern / Minimalist
• Professional / Business
• Tech / Futuristic
• Clean with plenty of whitespace

Tone of voice:
Clear, positive and customer-focused. Practical and accessible business style aimed at communicating concrete value for users.

Design inspiration — please review these websites:
• orbantal.com
• ravelo.app
• quendo.com
• tirameld.com
• gonwisp.com
What We DON'T Want
• Bold / In-your-face
• Dense / Compact
• Trendy / Experimental
• Childlike / Cheerful
• Playful / Cartoonish
• Busy / Chaotic
Colors
Use the color palette from velorix.com (blues, whites, clean professional tones).
[Exact hex codes used for element on the website:
#344054;
#1a1b1f;
#0254ac
#002249;
#e5edf7;
background-color: #fff; ]
Competitors (for context only — do NOT copy)
• brinvolt.nl
• kelmarin.com
• dortavecrm.com
• wexalunda.com
Budget
$150
Deadline
January 26, 2026

```html
<!DOCTYPE html>
<html lang="en">
<head>
<meta charset="utf-8">
<title>VeloRix Flyer</title>
<link rel="stylesheet" href="https://fonts.googleapis.com/css2?family=Lexend:wght@400;500;600&family=Lexend+Exa:wght@500;600;700&display=swap">
<style>
  :root {
    --stage: #1a8fd0;
    --paper: #ffffff;
    --navy: #10204f;
    --blue: #1b9ad6;
    --ink: #1a1b1f;
    --faint: #f2f3f5;
    --sky: #5ab8ea;
    --sky-pale: #eaf5fc;
    --photo-top: #5a5e66;
    --photo-bottom: #34363c;
    --aqua: #6fd0e6;
    --aqua-soft: #c4ecf5;
  }
  * { box-sizing: border-box; margin: 0; padding: 0; }
  html, body { width: 1200px; height: 777px; overflow: hidden; }
  body { background: var(--stage); font-family: "Lexend", sans-serif; }

  .canvas { position: relative; width: 1200px; height: 777px; overflow: hidden; background: var(--stage); }
  .flyer { position: absolute; left: 0; top: 51px; width: 1200px; height: 675px; background: var(--paper); overflow: hidden; }

  .brand { position: absolute; left: 89px; top: 98px; display: flex; align-items: center; gap: 12px; }
  .brand-dot { width: 40px; height: 40px; border-radius: 50%; background: var(--blue); }
  .brand-name { font-family: "Lexend Exa", sans-serif; font-weight: 600; font-size: 30px; color: var(--navy); }

  .backdrop-disc { position: absolute; left: 422px; top: 111px; width: 281px; height: 281px; border-radius: 50%; background: var(--faint); }

  .headline { position: absolute; left: 86px; top: 0; font-weight: inherit; }
  .headline span { position: absolute; left: 0; white-space: nowrap; line-height: 1; }
  .hl-crm { top: 212px; font-family: "Lexend Exa", sans-serif; font-weight: 600; font-size: 80px; color: var(--blue); letter-spacing: -4px; }
  .hl-adapts { top: 295px; font-family: "Lexend", sans-serif; font-weight: 500; font-size: 45px; color: var(--navy); letter-spacing: -1px; }
  .hl-how { top: 350px; font-family: "Lexend Exa", sans-serif; font-weight: 600; font-size: 60px; color: var(--blue); letter-spacing: -4px; }
  .hl-work { top: 410px; font-family: "Lexend Exa", sans-serif; font-weight: 700; font-size: 84px; color: var(--navy); letter-spacing: -6px; }

  .cta-primary { position: absolute; left: 86px; top: 510px; width: 244px; height: 58px; border: 1.5px solid var(--blue); border-radius: 5px; background: linear-gradient(180deg, #ffffff 40%, #d9eefa 100%); color: var(--blue); font-size: 24px; font-weight: 500; letter-spacing: -0.6px; display: flex; align-items: center; justify-content: center; }
  .cta-secondary { position: absolute; left: 106px; top: 565px; width: 205px; height: 58px; border-radius: 4px; background: var(--navy); color: #fff; font-size: 24px; font-weight: 500; letter-spacing: -0.6px; display: flex; align-items: center; justify-content: center; transform: rotate(-2.2deg); }

  .photo-area { position: absolute; left: 457px; top: 64px; width: 362px; height: 611px; background: linear-gradient(180deg, var(--photo-top) 0%, var(--photo-bottom) 100%); }

  .subline-card { position: absolute; left: 769px; top: 64px; width: 247px; height: 255px; border-radius: 12px 12px 0 0; background: linear-gradient(180deg, var(--sky) 0%, #9fd3f1 55%, var(--sky-pale) 100%); }
  .subline { position: absolute; left: 35px; top: 56px; font-size: 24px; font-weight: 500; line-height: 31.5px; color: var(--navy); letter-spacing: -0.7px; }

  .ornament-area { position: absolute; left: 979px; top: 176px; width: 221px; height: 274px; border-radius: 14px 0 0 14px; background: linear-gradient(160deg, var(--aqua) 0%, var(--aqua-soft) 100%); }

  .contact { position: absolute; left: 834px; top: 445px; }
  .contact-title { display: flex; align-items: center; gap: 12px; font-size: 25px; font-weight: 600; color: var(--blue); letter-spacing: -0.5px; line-height: 31px; }
  .contact-list { list-style: none; margin-top: 14px; }
  .contact-list li { display: flex; align-items: center; gap: 13px; font-size: 24px; color: var(--ink); letter-spacing: -0.3px; line-height: 31px; }
  .contact-list svg { width: 17px; height: 17px; flex: none; }
</style>
</head>
<body>
<div class="canvas">
  <main class="flyer">
    <div class="backdrop-disc"></div>

    <div class="brand">
      <span class="brand-dot"></span>
      <span class="brand-name">VeloRix</span>
    </div>

    <h1 class="headline">
      <span class="hl-crm">CRM</span>
      <span class="hl-adapts">That AdaptsTo</span>
      <span class="hl-how">HOW YOU</span>
      <span class="hl-work">WORK.</span>
    </h1>

    <div class="cta-primary">See it in action</div>
    <div class="cta-secondary">book a call</div>

    <div class="photo-area" role="img" aria-label="Portrait photo of a smiling businessman in a dark suit with arms crossed"></div>

    <div class="subline-card">
      <p class="subline">Discover how<br>VeloRix<br>simplifies your<br>sales process.</p>
    </div>

    <div class="ornament-area" role="img" aria-label="Decorative translucent aqua 3D shape"></div>

    <section class="contact">
      <h2 class="contact-title">
        <svg width="18" height="16" viewBox="0 0 18 16" fill="none" stroke="#10204f" stroke-width="2" stroke-linecap="round" stroke-linejoin="round"><path d="M2 3l12 10M14 5v8H6"/></svg>
        Reach Us!
      </h2>
      <ul class="contact-list">
        <li>
          <svg viewBox="0 0 24 24"><path fill="#10204f" d="M6.6 10.8a15.1 15.1 0 006.6 6.6l2.2-2.2a1 1 0 011-.25 11.4 11.4 0 003.6.57 1 1 0 011 1V20a1 1 0 01-1 1A17 17 0 013 4a1 1 0 011-1h3.5a1 1 0 011 1c0 1.25.2 2.45.57 3.57a1 1 0 01-.25 1z"/></svg>
          023-5718469
        </li>
        <li>
          <svg viewBox="0 0 24 24"><rect x="2" y="5" width="20" height="14" rx="2" fill="#10204f"/><path d="M3 6.5l9 6 9-6" fill="none" stroke="#fff" stroke-width="1.8"/></svg>
          hello@velorix.nl
        </li>
        <li>
          <svg viewBox="0 0 24 24"><path fill="#10204f" d="M5 2l14 11-6.2.8 3.6 7.2-2.6 1.2-3.5-7.2L5 19z"/></svg>
          velorix.com
        </li>
      </ul>
    </section>
  </main>
</div>
</body>
</html>
```